website name will be called www.nextridgepower.com
Please us color red, white,grey if possible
We are a solar provider that will offer solar ownership and leases with 25yr warranty and labor. Over 20yrs combined solar experience

Number of Pages Required

1 page

```html
<!DOCTYPE html>
<html lang="en">
<head>
<meta charset="utf-8">
<title>Nextridge Power – Solar Energy</title>
<link href="https://fonts.googleapis.com/css2?family=Poppins:wght@400;500;600;700&display=swap" rel="stylesheet">
<style>
:root{
  --red:#c4000b;
  --red-deep:#a80008;
  --red-band:#b8000a;
  --ink:#1b1b1b;
  --text:#555;
  --grey-bg:#f1f1f1;
  --line:#e3e3e3;
  --white:#fff;
}
*{box-sizing:border-box;margin:0;padding:0}
html,body{width:1200px;height:3906px;overflow:hidden}
body{font-family:'Poppins',sans-serif;color:var(--ink);background:var(--white);position:relative}
section,header,footer{position:relative;width:1200px;overflow:hidden}
.abs{position:absolute}
.btn{position:absolute;display:flex;align-items:center;justify-content:center;border-radius:20px;font-size:10px;font-weight:600}
.btn-red{background:var(--red);color:#fff}
.btn-outline{border:1.5px solid var(--red);color:var(--ink);background:#fff}
.btn-white{background:#fff;color:var(--red-deep)}
.sec-title{position:absolute;left:0;width:1200px;text-align:center;font-size:21px;font-weight:700;text-transform:uppercase}
.divider{position:absolute;width:50px;height:6px}
.divider::before{content:"";position:absolute;left:0;right:0;top:2.5px;height:1px;background:var(--red)}
.divider::after{content:"";position:absolute;left:22px;top:0;width:6px;height:6px;border-radius:50%;background:var(--red)}
.divider.light::before{background:#fff}.divider.light::after{background:#fff}
.center-div{left:575px}
.small{font-size:9px;line-height:18px;color:var(--text)}
.ph{position:absolute}

/* header */
.site-header{height:63px;border-bottom:1px solid var(--line)}
.brand{position:absolute;left:249px;top:20px;font-size:18px;font-weight:600;color:var(--red)}
.nav{position:absolute;top:24px;left:467px;display:flex;gap:0;font-size:10.5px;font-weight:500}
.nav span{position:absolute;white-space:nowrap}
.search{position:absolute;left:815px;top:24px}

/* hero */
.hero{height:357px}
.eyebrow{position:absolute;left:249px;top:75px;font-size:14px;letter-spacing:3px;color:var(--red);font-weight:500}
.eyebrow::after{content:"";position:absolute;left:155px;top:9px;width:55px;height:1px;background:var(--red)}
.hero h1{position:absolute;left:249px;top:97px;font-size:29px;line-height:42px;font-weight:700;text-transform:uppercase}
.hero p{position:absolute;left:249px;top:184px;width:360px;font-size:10px;line-height:18px;color:#333}

/* spectrum */
.spectrum{height:318px;background:var(--grey-bg)}
.card{position:absolute;top:118px;width:162px;height:140px;background:#f6f6f6;border:1px solid var(--line);border-radius:8px;text-align:center}
.card.active{background:#fff;box-shadow:0 6px 18px rgba(0,0,0,.1);border-color:#fff}
.card .ic{width:80px;height:80px;border-radius:50%;background:#e6e6e6;margin:18px auto 0;display:flex;align-items:center;justify-content:center}
.card.active .ic{background:var(--red)}
.card h4{font-size:11px;font-weight:500;margin-top:14px}

/* advantages */
.advantages{height:391px}
.adv-title{position:absolute;left:249px;top:58px;font-size:21px;font-weight:700;text-transform:uppercase}
.adv-item{position:absolute;left:249px;width:290px;height:50px}
.adv-item .ic{position:absolute;left:0;top:0;width:40px;height:40px;border-radius:50%;background:#f3e5e6}
.adv-item h5{position:absolute;left:50px;top:0;font-size:11.5px;font-weight:500}
.adv-item p{position:absolute;left:50px;top:17px;font-size:8.5px;line-height:15px;color:var(--text);width:240px}

/* consult */
.consult{height:311px;background:linear-gradient(90deg,var(--red-deep),var(--red-band) 55%,#a5000a)}
.consult h2{position:absolute;left:698px;top:92px;font-size:21px;line-height:26px;color:#fff;font-weight:700;text-transform:uppercase}
.consult p{position:absolute;left:698px;top:168px;width:230px;font-size:8.5px;line-height:19px;color:#fff}

/* projects */
.projects{height:625px}
.filters{position:absolute;top:148px;left:0;width:1200px}
.chip{position:absolute;height:26px;border-radius:13px;background:#ececec;font-size:9.5px;display:flex;align-items:center;justify-content:center;font-weight:500}
.chip.on{background:var(--red);color:#fff}
.tile{position:absolute;width:171px;height:180px}

/* why */
.why{height:478px;background:var(--grey-bg)}
.why-item{position:absolute;height:56px;display:flex;align-items:center;gap:14px;font-size:13.5px;line-height:18px;font-weight:500;color:#333}
.why-item .ic{width:50px;height:50px;border-radius:50%;background:#e5e5e5;flex:none;display:flex;align-items:center;justify-content:center}
.why-item.right{text-align:right}

/* contact */
.contact{height:425px;background:linear-gradient(90deg,var(--red-band),#b6000a 60%,#a9000a)}
.contact h2{position:absolute;left:249px;top:57px;font-size:21px;font-weight:700;color:#fff;text-transform:uppercase}
.contact p{position:absolute;left:249px;top:98px;width:300px;font-size:8.5px;line-height:19px;color:#fff}
.field{position:absolute;background:#c60812;border:1px solid #d21a22;border-radius:4px;color:#fff;font-size:9.5px;padding:8px 17px}

/* testimonials */
.testimonials{height:360px}
.testimonials .sec-title{text-transform:none;font-size:22px;font-weight:600}
.quote-card{position:absolute;top:122px;width:341px;height:178px;border:1px solid var(--line);border-radius:8px;background:#fff}
.quote-card .qm{position:absolute;left:17px;top:-16px;width:30px;height:30px;border-radius:50%;background:var(--red-deep);color:#fff;font-size:16px;font-weight:700;display:flex;align-items:center;justify-content:center}
.quote-card p{position:absolute;left:29px;top:26px;width:290px;font-size:10px;line-height:17px;color:#666}
.quote-card .avatar{position:absolute;left:17px;top:110px;width:52px;height:52px;border-radius:50%;border:3px solid var(--red);background:#d9c2b0}
.quote-card h6{position:absolute;left:81px;top:120px;font-size:11px;font-weight:600}
.quote-card small{position:absolute;left:81px;top:138px;font-size:9px;font-weight:600;color:#333}
.arrow{position:absolute;top:171px;width:36px;height:36px;border-radius:50%;display:flex;align-items:center;justify-content:center}

/* newsletter */
.newsletter{height:212px;background:var(--grey-bg)}
.newsletter .sec-title{text-transform:none;font-size:22px;font-weight:600}
.newsletter .sub{position:absolute;left:0;width:1200px;top:90px;text-align:center;font-size:12px;color:#333}
.nl-input{position:absolute;left:400px;top:120px;width:400px;height:33px;background:#fff;border-radius:17px;font-size:9px;color:#aaa;padding:10px 18px}

/* footer */
.site-footer{height:340px;background:linear-gradient(90deg,var(--red-deep),var(--red-band) 60%,#a9000a);color:#fff}
.foot-brand{position:absolute;left:0;width:1200px;top:88px;text-align:center;font-size:19px;font-weight:600}
.socials{position:absolute;left:540px;top:135px;display:flex;gap:12px}
.socials span{width:22px;height:22px;border-radius:50%;background:#fff}
.foot-line{position:absolute;left:249px;width:702px;top:165px;height:1px;background:rgba(255,255,255,.35)}
.foot-nav span{position:absolute;top:184px;font-size:10.5px;font-weight:500}
.contact-block{position:absolute;top:248px;height:46px}
.contact-block .ic{position:absolute;left:0;top:0;width:42px;height:42px;border-radius:50%;background:#fff;display:flex;align-items:center;justify-content:center}
.contact-block b{position:absolute;left:50px;top:2px;font-size:12px;font-weight:600;white-space:nowrap}
.contact-block span{position:absolute;left:50px;top:20px;font-size:9.5px;line-height:13px;white-space:nowrap}
.vsep{position:absolute;top:244px;width:1px;height:50px;background:rgba(255,255,255,.35)}
.bottom-bar{position:absolute;left:0;top:3880px;width:1200px;height:26px;background:#e9e9e9;font-size:9px;color:#444}
.bottom-bar span{position:absolute;top:7px}
</style>
</head>
<body>

<header class="site-header">
  <div class="brand">Nextridge Power</div>
  <nav class="nav">
    <span style="left:0">Home</span>
    <span style="left:53px">About</span>
    <span style="left:105px">Services ▾</span>
    <span style="left:170px">Projects</span>
    <span style="left:230px">Blogs</span>
    <span style="left:281px">Contactus</span>
  </nav>
  <svg class="search" width="14" height="14" viewBox="0 0 14 14"><circle cx="6" cy="6" r="4.5" fill="none" stroke="#222" stroke-width="1.4"/><line x1="9.3" y1="9.3" x2="13" y2="13" stroke="#222" stroke-width="1.4"/></svg>
  <div class="btn btn-red" style="left:846px;top:16px;width:104px;height:32px">Free Quote</div>
</header>

<section class="hero">
  <div class="eyebrow">SOLAR SYSTEM</div>
  <h1>Safe, Clean &amp;<br>Renewable Energy</h1>
  <p>Lorem ipsum dolor sit amet, consectetur adipiscing elit, sed do eiusmod tempor incididunt ut labore et dolore magna aliqua.</p>
  <div class="btn btn-outline" style="left:249px;top:232px;width:105px;height:32px">More About us</div>
  <div class="btn btn-red" style="left:360px;top:232px;width:104px;height:32px">Our Services</div>
  <div class="ph" role="img" aria-label="Illustration of a house with trees and solar panels on a floating island under a sun" style="left:640px;top:38px;width:315px;height:295px;border-radius:45% 45% 50% 50%;background:radial-gradient(circle at 50% 45%,#9ccf5c 0,#6aa84f 40%,#b98c5a 62%,#f7f2ea 64%)"></div>
  <svg class="abs" style="left:584px;top:292px" width="32" height="40" viewBox="0 0 32 40"><rect x="1" y="1" width="30" height="38" rx="15" fill="#fff" stroke="#e2e2e2"/><rect x="11" y="10" width="10" height="18" rx="5" fill="none" stroke="var(--red)" stroke-width="1.4"/></svg>
</section>

<section class="spectrum">
  <div class="sec-title" style="top:54px">We Cover The Whole Spectrum</div>
  <div class="divider center-div" style="top:84px"></div>
  <div class="card" style="left:249px"><div class="ic"><svg width="36" height="30" viewBox="0 0 36 30" fill="none" stroke="#333" stroke-width="1.3"><circle cx="10" cy="6" r="3"/><rect x="6" y="13" width="16" height="11"/><line x1="14" y1="13" x2="14" y2="24"/><line x1="6" y1="18" x2="22" y2="18"/><rect x="24" y="6" width="9" height="9"/></svg></div><h4>NON-POLLUTING</h4></div>
  <div class="card active" style="left:429px"><div class="ic"><svg width="38" height="32" viewBox="0 0 38 32" fill="none" stroke="#fff" stroke-width="1.4"><rect x="10" y="2" width="18" height="10"/><line x1="19" y1="2" x2="19" y2="12"/><line x1="10" y1="7" x2="28" y2="7"/><rect x="4" y="18" width="30" height="12"/><line x1="19" y1="12" x2="19" y2="18"/></svg></div><h4>EASY INSTALLATION</h4></div>
  <div class="card" style="left:609px"><div class="ic"><svg width="38" height="32" viewBox="0 0 38 32" fill="none" stroke="#333" stroke-width="1.3"><circle cx="19" cy="6" r="3.5"/><rect x="5" y="15" width="28" height="13"/><line x1="14" y1="15" x2="14" y2="28"/><line x1="24" y1="15" x2="24" y2="28"/><line x1="5" y1="21" x2="33" y2="21"/></svg></div><h4>RENEWABLE ENERGY</h4></div>
  <div class="card" style="left:789px"><div class="ic"><svg width="38" height="32" viewBox="0 0 38 32" fill="none" stroke="#333" stroke-width="1.3"><rect x="4" y="8" width="30" height="20" rx="2"/><rect x="12" y="3" width="14" height="5"/><circle cx="19" cy="18" r="4"/></svg></div><h4>SOLAR MAINTENANCE</h4></div>
</section>

<section class="advantages">
  <div class="adv-title">Discover The Advantages</div>
  <div class="divider" style="left:249px;top:88px"></div>
  <div class="adv-item" style="top:108px"><div class="ic"></div><h5>Save Your Money</h5><p>Lorem ipsum dolor sit amet, consectetur adipiscing elit, sed do eiusmod tempor incididunt ut.</p></div>
  <div class="adv-item" style="top:173px"><div class="ic"></div><h5>5 Stars Customer Services</h5><p>Lorem ipsum dolor sit amet, consectetur adipiscing elit, sed do eiusmod tempor incididunt ut.</p></div>
  <div class="adv-item" style="top:238px"><div class="ic"></div><h5>Your Home is Energy</h5><p>Lorem ipsum dolor sit amet, consectetur adipiscing elit, sed do eiusmod tempor incididunt ut.</p></div>
  <div class="btn btn-outline" style="left:249px;top:299px;width:105px;height:32px;color:var(--red)">View All</div>
  <div class="ph" role="img" aria-label="Illustration of three teal solar panels on stands over a strip of grass" style="left:570px;top:102px;width:380px;height:180px;border-radius:6px;background:linear-gradient(160deg,#3b8c93,#1f5f66 60%,#6aa84f)"></div>
</section>

<section class="consult">
  <div class="ph" role="img" aria-label="Red company service van" style="left:230px;top:50px;width:360px;height:210px;border-radius:40px 60px 20px 20px;background:linear-gradient(180deg,#e23a3f,#b8141a 70%,#2a2a2a)"></div>
  <svg class="abs" style="left:870px;top:55px" width="110" height="110" viewBox="0 0 110 110"><path d="M20 12 A52 52 0 0 1 70 100" fill="none" stroke="#fff" stroke-width="3"/></svg>
  <h2>Get Free Consultancy<br>About Your Project</h2>
  <div class="divider light" style="left:698px;top:148px"></div>
  <p>Lorem ipsum dolor sit amet, consectetur adipiscing sed do eiusmod tempor incididunt ut labore et</p>
  <div class="btn btn-white" style="left:698px;top:220px;width:104px;height:31px">Free Quote</div>
</section>

<section class="projects">
  <div class="sec-title" style="top:57px">Our Incredible Projects</div>
  <div class="divider center-div" style="top:87px"></div>
  <div class="small" style="position:absolute;left:450px;top:99px;width:300px;text-align:center">Lorem ipsum dolor sit amet, consectetur adipiscing sed do eiusmod tempor incididunt ut labore et</div>
  <div class="filters">
    <div class="chip on" style="left:426px;width:42px">All</div>
    <div class="chip" style="left:479px;width:92px">Household</div>
    <div class="chip" style="left:581px;width:92px">Solar Panels</div>
    <div class="chip" style="left:683px;width:92px">Wind Energy</div>
  </div>
  <div class="tile" role="img" aria-label="Worker installing solar panels on a roof" style="left:249px;top:204px;background:linear-gradient(150deg,#cfd9e4,#3a4d66)"></div>
  <div class="tile" style="left:426px;top:204px;background:linear-gradient(180deg,#c81a1e,#b3070d);color:#fff;font-size:10px;font-weight:500;display:flex;align-items:center;justify-content:center">Project</div>
  <div class="tile" role="img" aria-label="Gloved hands wiring a solar panel" style="left:603px;top:204px;background:linear-gradient(150deg,#8d98a6,#39424f)"></div>
  <div class="tile" role="img" aria-label="White house front with gable roof" style="left:780px;top:204px;background:linear-gradient(180deg,#b9cde2,#7f8b96 60%,#6f7a5a)"></div>
  <div class="tile" role="img" aria-label="Brick house with rooftop solar panels" style="left:249px;top:391px;background:linear-gradient(180deg,#c7d3de,#3f4756 45%,#7a4334)"></div>
  <div class="tile" role="img" aria-label="Residential rooftops with solar panels" style="left:426px;top:391px;background:linear-gradient(180deg,#8ba7c2,#7e8a90 60%,#4e5a3c)"></div>
  <div class="tile" role="img" aria-label="House roof against a pale sky" style="left:603px;top:391px;background:linear-gradient(180deg,#e6e6ea,#c8c3c4 55%,#4a4038)"></div>
  <div class="tile" role="img" aria-label="Technician working among rooftop solar panels" style="left:780px;top:391px;background:linear-gradient(150deg,#b9c9dc,#2c4a77)"></div>
</section>

<section class="why">
  <div class="sec-title" style="top:55px">Why Choose Us Solar Energy</div>
  <div class="divider center-div" style="top:85px"></div>
  <div class="small" style="position:absolute;left:450px;top:97px;width:300px;text-align:center">Lorem ipsum dolor sit amet, consectetur adipiscing sed do eiusmod tempor incididunt ut labore et</div>
  <div class="why-item" style="left:249px;top:172px"><div class="ic"></div><span>Long Time<br>to Use</span></div>
  <div class="why-item" style="left:249px;top:262px"><div class="ic"></div><span>Always Clean<br>Energy</span></div>
  <div class="why-item" style="left:249px;top:352px"><div class="ic"></div><span>Energy Can Be<br>Re-used</span></div>
  <div class="why-item right" style="right:249px;top:178px"><span>Low Installation<br>Costs</span><div class="ic"></div></div>
  <div class="why-item right" style="right:249px;top:262px"><span>Easy<br>Installation</span><div class="ic"></div></div>
  <div class="why-item right" style="right:249px;top:352px"><span>Used for<br>Many Purposes</span><div class="ic"></div></div>
  <div class="ph" role="img" aria-label="Illustration of a solar panel and two wind turbines on a grassy floating island" style="left:455px;top:165px;width:290px;height:255px;border-radius:40% 40% 50% 50%;background:radial-gradient(circle at 50% 40%,#2f3f9a 0,#3b4fb5 25%,#5fae3e 50%,#8a5a34 70%,transparent 72%)"></div>
</section>

<section class="contact">
  <h2>Fill Free Contact Us</h2>
  <div class="divider light" style="left:249px;top:89px"></div>
  <p>Lorem ipsum dolor sit amet, consectetur adipiscing sed do eiusmod tempor incididunt ut labore et</p>
  <div class="field" style="left:249px;top:147px;width:341px;height:28px">Name*</div>
  <div class="field" style="left:249px;top:188px;width:165px;height:28px">Your Phone*</div>
  <div class="field" style="left:426px;top:188px;width:164px;height:28px">Your Phone*</div>
  <div class="field" style="left:249px;top:230px;width:341px;height:90px">Name*</div>
  <div class="btn btn-white" style="left:249px;top:333px;width:105px;height:31px">Submit Now</div>
  <div class="ph" role="img" aria-label="Folding portable solar panel on a stand with green leaves" style="left:640px;top:77px;width:320px;height:270px;border-radius:10px;background:linear-gradient(150deg,#d9d9d9,#1b2233 20%,#111827 75%,#5c9b3a)"></div>
</section>

<section class="testimonials">
  <div class="sec-title" style="top:54px">What Our Clients Says</div>
  <div class="divider center-div" style="top:86px"></div>
  <div class="arrow" style="left:194px;border:1.5px solid var(--red)"><svg width="10" height="10" viewBox="0 0 10 10"><path d="M6.5 1.5 3 5l3.5 3.5" fill="none" stroke="var(--red)" stroke-width="1.4"/></svg></div>
  <div class="quote-card" style="left:249px"><div class="qm">“</div><p>Duis aute irure dolor in reprehenderit in voluptate velit esse cillum dolore eu fugiat nulla pariatur. Excepteur sint occaecat cupidatat non proident, sunt in culpa qui officia deserunt.</p><div class="avatar" role="img" aria-label="Client portrait"></div><h6>MARA ELLING</h6><small>(Software Developer)</small></div>
  <div class="quote-card" style="left:609px"><div class="qm">“</div><p>Duis aute irure dolor in reprehenderit in voluptate velit esse cillum dolore eu fugiat nulla pariatur. Excepteur sint occaecat cupidatat non proident, sunt in culpa qui officia deserunt.</p><div class="avatar" role="img" aria-label="Client portrait"></div><h6>TOBIAS RENWICK</h6><small>(Managing Director)</small></div>
  <div class="arrow" style="left:968px;background:var(--red-deep)"><svg width="10" height="10" viewBox="0 0 10 10"><path d="M3.5 1.5 7 5 3.5 8.5" fill="none" stroke="#fff" stroke-width="1.4"/></svg></div>
</section>

<section class="newsletter">
  <div class="sec-title" style="top:42px">Subscribe Our News Letter</div>
  <div class="divider center-div" style="top:74px"></div>
  <div class="sub">Subscribe To Our NewsLetter To Receive The Latest News Letter And Exclusive Offer Every Week</div>
  <div class="nl-input">Your Email address</div>
  <div class="btn btn-red" style="left:686px;top:120px;width:114px;height:33px;border-radius:17px;font-size:9.5px">SUBCRIBE NOW</div>
</section>

<footer class="site-footer">
  <div class="foot-brand">Nextridge Power</div>
  <div class="socials"><span></span><span></span><span></span><span></span></div>
  <div class="foot-line"></div>
  <div class="foot-nav">
    <span style="left:380px">Home</span><span style="left:453px">About</span><span style="left:528px">Services</span>
    <span style="left:613px">Projects</span><span style="left:696px">Blogs</span><span style="left:768px">Contactus</span>
  </div>
  <div class="contact-block" style="left:279px"><div class="ic"><svg width="16" height="16" viewBox="0 0 16 16"><path d="M4 1.5l2.2 3-1.4 1.6c.8 1.9 2.2 3.3 4.1 4.1l1.6-1.4 3 2.2-1 2.5C7 13.5 2.5 9 1.5 3z" fill="var(--red)"/></svg></div><b>Call Us Now</b><span>555 010 2468 900</span></div>
  <div class="vsep" style="left:486px"></div>
  <div class="contact-block" style="left:508px"><div class="ic"><svg width="14" height="18" viewBox="0 0 14 18"><path d="M7 1a5.5 5.5 0 0 0-5.5 5.5C1.5 11 7 17 7 17s5.5-6 5.5-10.5A5.5 5.5 0 0 0 7 1z" fill="var(--red)"/><circle cx="7" cy="6.5" r="2" fill="#fff"/></svg></div><b>Address</b><span>48 Ridgeway Lane,<br>Helio Court, Springfield</span></div>
  <div class="vsep" style="left:720px"></div>
  <div class="contact-block" style="left:736px"><div class="ic"><svg width="18" height="18" viewBox="0 0 18 18"><circle cx="9" cy="9" r="3" fill="none" stroke="var(--red)" stroke-width="1.8"/><path d="M12 6v4.5a2 2 0 0 0 4 0V9a7 7 0 1 0-3 5.7" fill="none" stroke="var(--red)" stroke-width="1.8"/></svg></div><b>Email Us</b><span>info@nextridgepower.com</span></div>
</footer>

<div class="bottom-bar"><span style="left:249px">© Copyrights 2025. All Rights Reserved. Nextridge Power</span><span style="right:249px">Website By Brightline Studio</span></div>

</body>
</html>
```